Coral Journey Mate - A Travel Services Website

Sunreef Home Rentals is a company that provides travels services to home owners and travellers to Barbados. Coral Journey Mate is a particular brand targeting travelling guests with specific set of travel services. The brand slogan is:

'Getting you the best for less'

The travel services will include:

- Coral Journey Mate Perks Pass
- Car Hire Quote Service
- Mobile Phone Sim Cards
- Prepaid Debit Cards
- Airport Hotel Booking
- Airport Lounge Booking
- Airport Parking

There will also be a travel planner function for guests.

The main puropse of the site is as follows:

1. Registration for the Coral Journey Mate Perks Pass

2. Creation of user account which the guest will frequently return to check for updates

3. Purchase of ancillary travel products and services

4. To use the Travel Planner

5. To gather data on holiday home owners in Barbados

A site map can be seen at the following link:

http://plotgridly.example/outlines/viewMap/4kqzvbn8ytrwpa2fuh5ximc07jldg6sqenoa9rvb33kf2pyq71

Webpage templates (2 required)

The first will be form control heavy (text boxes, checkboxes ect). It will need failure and success messages / indicators etc.

The second will be a general content area with a secondary navigation area (i.e for sub sections of the current section). This will house text / headings and images.

Both will require header, primary navigation, content and footer areas.

N.B. Please not that I am not technical and the above webtemplate narrative has been supplied by my web developer/programmer. If you have any questions, please ask me any questions and I will get an answer from him.

Target Market(s)

My customers tend to be:

Sex: Female
Age: 24-55
Location: UK, USA, Canada
Social Class: A,B,C1
Income: Medium income bracket

They are possibly visiting Barbados for the first and only time. It is an expensive destination and is accessible to people with a medium to high income. They still desire 'value for money'. Therefore the sight must give guests confidence that Coral Journey Mate is 'their friend', is seeking to offer the best value deals for their vacation/holiday.

Industry/Entity Type

Travel

Requirements
Must have
• The site templates must be professional, aspirational, trustworthy, reassuring, clean, innovative, fun. When people visit the site they should be excited about the savings that they can make and want to return as there is a perceived benefit for them. It must look expensive and professional in its projected image.
Nice to have
• Smooth currved lines, seperated boxed areas for content, as simple and uncluttered layout and it must be simple to read!
Should not have
• It should not be cartoonly, despite my attached logo and must not look cheap.

```html
<!DOCTYPE html>
<html lang="en">
<head>
<meta charset="utf-8">
<title>Coral Journey Mate – Confirmed Bookings</title>
<link rel="stylesheet" href="https://fonts.googleapis.com/css2?family=Source+Sans+3:wght@400;600;700&display=swap">
<style>
  :root {
    --sea-deep: #0a6f97;
    --frame-white: #ffffff;
    --panel-veil: rgba(235, 245, 248, 0.72);
    --btn-top: #55c7ea;
    --btn-bottom: #0b7eae;
    --title-blue: #1a9ad9;
    --text-grey: #555b60;
    --label-grey: #6d7377;
    --rule-grey: rgba(110, 120, 125, 0.45);
    --brand-red: #d81e2a;
  }
  * { box-sizing: border-box; margin: 0; padding: 0; }
  html, body { width: 1200px; height: 900px; overflow: hidden; }
  body {
    position: relative;
    font-family: "Source Sans 3", Arial, sans-serif;
    background: var(--sea-deep);
  }
  .backdrop {
    position: absolute; inset: 0;
    background:
      radial-gradient(ellipse at 80% 55%, rgba(255,255,255,0.35), transparent 55%),
      linear-gradient(180deg, #0c7aa3 0%, #2b9cc2 35%, #7cc6dc 62%, #d8ecef 78%, #4b9fb8 100%);
  }

  /* Login */
  .login { position: absolute; top: 16px; left: 810px; width: 345px; height: 42px; }
  .login-label { position: absolute; top: 0; font-size: 13px; color: var(--frame-white); }
  .login-label.user { left: 25px; }
  .login-label.pass { left: 152px; }
  .login-field {
    position: absolute; top: 17px; width: 118px; height: 22px;
    background: var(--frame-white); border: none; border-radius: 11px;
  }
  .login-field.user { left: 0; }
  .login-field.pass { left: 122px; }
  .login-button { position: absolute; top: 17px; left: 244px; width: 97px; height: 24px; }

  /* Header */
  .header-frame {
    position: absolute; left: 26px; top: 70px; width: 1146px; height: 181px;
    border: 2px solid var(--frame-white); border-radius: 16px;
    background: linear-gradient(180deg, rgba(20,110,150,0.55), rgba(60,170,205,0.35));
  }
  .brand {
    position: absolute; left: 60px; top: 92px; display: flex; align-items: center; gap: 18px;
  }
  .brand-dot { width: 70px; height: 70px; border-radius: 50%; background: var(--brand-red); }
  .brand-name {
    font-weight: 700; font-size: 54px; line-height: 54px; color: var(--brand-red);
  }
  .snapshot {
    position: absolute; border: 6px solid var(--frame-white);
    box-shadow: 0 3px 8px rgba(0,0,0,0.3);
  }
  .snapshot.hammock { left: 502px; top: 45px; width: 243px; height: 143px; transform: rotate(3deg);
    background: linear-gradient(180deg, #4fa9e0 0%, #7ec4e6 55%, #e9e3d2 100%); }
  .snapshot.catamaran { left: 692px; top: 76px; width: 234px; height: 166px; transform: rotate(-5deg);
    background: linear-gradient(160deg, #2bb3c7 0%, #5dcad6 50%, #c9c7bd 100%); }
  .snapshot.snorkel { left: 920px; top: 66px; width: 222px; height: 180px; transform: rotate(6deg);
    background: linear-gradient(180deg, #3aa0d8 0%, #1f7fc0 100%); }

  /* Buttons */
  .pill {
    display: flex; align-items: center; justify-content: center;
    border: 1.5px solid var(--frame-white); border-radius: 12px;
    background: linear-gradient(180deg, var(--btn-top), var(--btn-bottom));
    color: var(--frame-white); font-size: 13px; white-space: nowrap;
    text-decoration: none;
  }
  .primary-nav {
    position: absolute; left: 52px; top: 260px; width: 1096px; height: 24px;
    display: flex; gap: 3px;
  }
  .primary-nav .pill { flex: 1; }

  /* Content */
  .content-frame {
    position: absolute; left: 26px; top: 294px; width: 1146px; height: 533px;
    border: 2px solid var(--frame-white); border-radius: 20px;
    background: rgba(255,255,255,0.12);
  }
  .content-panel {
    position: absolute; left: 47px; top: 315px; width: 1107px; height: 491px;
    border: 1.5px solid var(--frame-white); border-radius: 16px;
    background: var(--panel-veil);
  }
  .page-title {
    position: absolute; left: 115px; top: 386px;
    font-size: 25px; font-weight: 400; color: var(--title-blue);
  }
  .bookings { position: absolute; left: 102px; top: 430px; width: 994px; }
  .bookings-head {
    position: relative; height: 18px; border-bottom: 1px solid var(--rule-grey);
    font-size: 11px; color: var(--label-grey);
  }
  .booking-row {
    position: relative; height: 33px; margin-top: 14px;
    border-top: 1px solid var(--rule-grey); border-bottom: 1px solid var(--rule-grey);
    font-size: 15px; color: var(--text-grey);
  }
  .booking-row:first-of-type { margin-top: 22px; }
  .cell { position: absolute; top: 50%; transform: translateY(-50%); white-space: nowrap; }
  .bookings-head .cell { top: 0; transform: none; }
  .c-pickup { left: 13px; }
  .c-pickdate { left: 115px; }
  .c-drop { left: 258px; }
  .c-dropdate { left: 369px; }
  .c-age { left: 493px; }
  .booking-row .c-age { left: 516px; }
  .c-group { left: 591px; }
  .c-currency { left: 720px; }
  .action-label { font-size: 11px; color: var(--label-grey); margin-top: 2px; }
  .a-view { left: 861px; }
  .a-cancel { left: 922px; }
  .tick-box {
    position: absolute; top: 50%; width: 22px; height: 18px; margin-top: -12px;
    background: var(--frame-white); border: 1px solid #b9c3c7; border-radius: 5px;
    box-shadow: 1px 2px 2px rgba(0,0,0,0.15);
  }
  .b-view { left: 890px; }
  .b-cancel { left: 964px; }

  /* Footer */
  .footer-frame {
    position: absolute; left: 28px; top: 820px; width: 1146px; height: 56px;
    border: 1.5px solid rgba(255,255,255,0.45); border-top: none;
    border-radius: 0 0 16px 16px;
  }
  .footer-nav {
    position: absolute; left: 297px; top: 841px; width: 609px; height: 24px;
    display: flex; gap: 2px;
  }
  .footer-nav .pill { flex: 1; }
</style>
</head>
<body>
  <div class="backdrop" role="img" aria-label="Tropical beach with palm trees, white sand and turquoise sea"></div>

  <form class="login">
    <span class="login-label user">User Name</span>
    <span class="login-label pass">Password</span>
    <input class="login-field user" type="text" aria-label="User Name">
    <input class="login-field pass" type="password" aria-label="Password">
    <a class="pill login-button" href="#">Log In</a>
  </form>

  <header>
    <div class="header-frame"></div>
    <div class="brand">
      <span class="brand-dot"></span>
      <span class="brand-name">Coral<br>Journey Mate</span>
    </div>
    <div class="snapshot hammock" role="img" aria-label="Hammock between palm trees on a beach"></div>
    <div class="snapshot catamaran" role="img" aria-label="Guests relaxing on a catamaran net over clear water"></div>
    <div class="snapshot snorkel" role="img" aria-label="Children snorkelling in blue water"></div>
  </header>

  <nav class="primary-nav">
    <a class="pill" href="#">Home</a>
    <a class="pill" href="#">Airport Parking</a>
    <a class="pill" href="#">Aiport Hotel</a>
    <a class="pill" href="#">Aiport Lounge</a>
    <a class="pill" href="#">Car Hire&nbsp; Travel</a>
    <a class="pill" href="#">Money&nbsp; Mobile</a>
    <a class="pill" href="#">Simcards</a>
    <a class="pill" href="#">Privelege Card</a>
    <a class="pill" href="#">Contact Us</a>
  </nav>

  <main>
    <div class="content-frame"></div>
    <div class="content-panel"></div>
    <h1 class="page-title">Confirmed Bookings</h1>

    <section class="bookings">
      <div class="bookings-head">
        <span class="cell c-pickup">Pick Up Location</span>
        <span class="cell c-pickdate">Date</span>
        <span class="cell c-drop">Drop Off Location</span>
        <span class="cell c-dropdate">Date</span>
        <span class="cell c-age">Driver's Age</span>
        <span class="cell c-group">Car Group</span>
        <span class="cell c-currency">Your Currency</span>
      </div>

      <div class="booking-row">
        <span class="cell c-pickup">David's Hotel</span><span class="cell c-pickdate">01/01/11</span>
        <span class="cell c-drop">David's Hotel</span><span class="cell c-dropdate">01/01/11</span>
        <span class="cell c-age">21</span><span class="cell c-group"></span>
        <span class="cell c-currency">English Pounds</span>
        <span class="cell action-label a-view">View</span><span class="tick-box b-view"></span>
        <span class="cell action-label a-cancel">Cancel</span><span class="tick-box b-cancel"></span>
      </div>
      <div class="booking-row">
        <span class="cell c-pickup">Airport</span><span class="cell c-pickdate">09/08/11</span>
        <span class="cell c-drop">Hotel</span><span class="cell c-dropdate">10/08/11</span>
        <span class="cell c-age">43</span><span class="cell c-group"></span>
        <span class="cell c-currency">English Pounds</span>
        <span class="cell action-label a-view">View</span><span class="tick-box b-view"></span>
        <span class="cell action-label a-cancel">Cancel</span><span class="tick-box b-cancel"></span>
      </div>
      <div class="booking-row">
        <span class="cell c-pickup">Hotel DLoan</span><span class="cell c-pickdate">09/05/11</span>
        <span class="cell c-drop">Airport</span><span class="cell c-dropdate">05/14/11</span>
        <span class="cell c-age">41</span><span class="cell c-group"></span>
        <span class="cell c-currency">English Pounds</span>
        <span class="cell action-label a-view">View</span><span class="tick-box b-view"></span>
        <span class="cell action-label a-cancel">Cancel</span><span class="tick-box b-cancel"></span>
      </div>
      <div class="booking-row">
        <span class="cell c-pickup">Skyward Rise</span><span class="cell c-pickdate">12/12/11</span>
        <span class="cell c-drop">Thrustwood BB</span><span class="cell c-dropdate">04/01/11</span>
        <span class="cell c-age">24</span><span class="cell c-group">Large Family</span>
        <span class="cell c-currency">English Pounds</span>
        <span class="cell action-label a-view">View</span><span class="tick-box b-view"></span>
        <span class="cell action-label a-cancel">Cancel</span><span class="tick-box b-cancel"></span>
      </div>
      <div class="booking-row">
        <span class="cell c-pickup">Shift O' Mart</span><span class="cell c-pickdate">11/20/11</span>
        <span class="cell c-drop">Bayhaven</span><span class="cell c-dropdate">03/12/11</span>
        <span class="cell c-age">55</span><span class="cell c-group">Van</span>
        <span class="cell c-currency">English Pounds</span>
        <span class="cell action-label a-view">View</span><span class="tick-box b-view"></span>
        <span class="cell action-label a-cancel">Cancel</span><span class="tick-box b-cancel"></span>
      </div>
      <div class="booking-row">
        <span class="cell c-pickup">Vagus</span><span class="cell c-pickdate">11/20/11</span>
        <span class="cell c-drop">Dbourgh</span><span class="cell c-dropdate">03/12/11</span>
        <span class="cell c-age">22</span><span class="cell c-group">Mini Economy</span>
        <span class="cell c-currency">English Pounds</span>
        <span class="cell action-label a-view">View</span><span class="tick-box b-view"></span>
        <span class="cell action-label a-cancel">Cancel</span><span class="tick-box b-cancel"></span>
      </div>
    </section>
  </main>

  <footer>
    <div class="footer-frame"></div>
    <nav class="footer-nav">
      <a class="pill" href="#">Home</a>
      <a class="pill" href="#">Contact Us</a>
      <a class="pill" href="#">Registration</a>
      <a class="pill" href="#">News</a>
      <a class="pill" href="#">Gallery</a>
    </nav>
  </footer>
</body>
</html>
```